Call to action redesign for ~1/3 of a website i.e. the hero image

We are redesigning just the top 1/3 of brelloway.net. We need to add in a box that solves the problems that are outlined in the attached pdf.

We're looking for extremely clean and easy to understand design options.

If we like your designs there is definitely potential for picking up steady work.

Target Market(s)

Businesses

Industry/Entity Type

Call

```html
<!DOCTYPE html>
<html lang="en">
<head>
<meta charset="utf-8">
<title>Brelloway – SEO Services</title>
<link rel="stylesheet" href="https://fonts.googleapis.com/css2?family=Oswald:wght@400;500&family=Arimo:wght@400;700&display=swap">
<style>
:root{
  --brand-blue:#2355a6;
  --link-blue:#1f62b5;
  --sky:#6cc6ec;
  --sky-lead:#7fcdee;
  --sky-edge:#a9e2f7;
  --page-bg:#f3f7fa;
  --ink:#333;
  --muted:#666;
  --nav:#555;
  --red:#e8141a;
  --accent-orange:#e5892a;
  --card-border:#d8e1e8;
}
*{margin:0;padding:0;box-sizing:border-box}
html,body{width:1200px;height:954px;overflow:hidden}
body{font-family:"Arimo",Arial,sans-serif;color:var(--ink);
  background:linear-gradient(90deg,#0a59b8 0%,#14a0e0 4%,#0c7ed0 8%,#0a5fbf 50%,#0c7ed0 92%,#14a0e0 96%,#0a59b8 100%);position:relative}
.page{position:absolute;left:96px;top:0;width:991px;height:954px;background:var(--page-bg);box-shadow:0 0 12px rgba(0,0,0,.35)}

.header{position:absolute;left:0;top:0;width:991px;height:74px;background:linear-gradient(#fff 0%,#f4f4f4 55%,#d8d8d8 100%);border-bottom:1px solid #c8c8c8}
.logo{position:absolute;left:38px;top:19px;font-size:29px;font-weight:700;letter-spacing:2px;color:var(--brand-blue)}
.nav{position:absolute;left:369px;top:30px;display:flex;gap:20px;font-size:14px;color:var(--nav)}
.phone{position:absolute;right:34px;top:28px;font-size:17px;font-weight:700;color:var(--brand-blue)}

.hero{position:absolute;left:13px;top:75px;width:964px;height:298px;border:1px solid #c9c9c9;background:#fff;overflow:hidden}
.hero-backdrop{position:absolute;left:0;top:0;width:620px;height:296px;background:linear-gradient(100deg,#dcdcf6 0%,#eeeefb 45%,#fff 100%)}
.hero-photo{position:absolute;left:0;top:0;width:182px;height:296px;background:linear-gradient(#e4e1ec,#b9b6c4)}
.hero-arrow{position:absolute;left:474px;width:140px;height:62px;background:linear-gradient(#fbeeee,#fdf6f6);border-radius:8px}
.search{position:absolute;left:178px;top:116px;width:428px;height:54px;background:#fff;border:2px solid #a5a5a5;border-radius:12px;box-shadow:0 2px 4px rgba(0,0,0,.2)}
.search span{position:absolute;left:20px;top:15px;font-size:19px;color:#777}
.search-btn{position:absolute;right:-2px;top:-2px;width:178px;height:54px;border-radius:12px;background:linear-gradient(#3aa2ea,#0b6dc8);color:#fff;font-size:16px;font-weight:700;line-height:18px;padding:9px 0 0 53px;box-shadow:0 2px 4px rgba(0,0,0,.3)}
.search-btn::before{content:"";position:absolute;left:12px;top:11px;width:30px;height:30px;border-radius:50%;background:#e7f3fc;border:2px solid #8cc6ef}
.search-btn::after{content:"";position:absolute;left:24px;top:20px;border-left:10px solid #0b6dc8;border-top:6px solid transparent;border-bottom:6px solid transparent}
.offer{position:absolute;left:625px;top:40px;font-family:"Oswald",sans-serif;font-weight:500;font-size:42px;line-height:47px;color:var(--brand-blue)}
.offer em{font-style:normal;color:var(--red)}
.offer-copy{position:absolute;left:627px;top:152px;width:310px;font-size:16px;line-height:19.5px;color:var(--muted)}

.stats{position:absolute;left:13px;top:378px;width:964px;height:70px;background:var(--sky);border:2px solid var(--sky-edge);color:#fff}
.stats-lead{position:absolute;left:0;top:0;width:290px;height:66px;background:var(--sky-lead);font-family:"Oswald",sans-serif;font-size:21px;line-height:23px;padding:9px 0 0 39px}
.stats-chevron{position:absolute;left:270px;top:0}
.stat{position:absolute;top:9px;font-size:15px}
.stat b{display:block;font-family:"Oswald",sans-serif;font-weight:500;font-size:28px;line-height:30px}
.stat-divider{position:absolute;top:10px;width:2px;height:46px;background:rgba(255,255,255,.45)}

.card{position:absolute;top:465px;width:310px;height:300px;background:#fff;border:2px solid var(--card-border);border-radius:14px;overflow:hidden}
.card h2{height:48px;background:linear-gradient(#fafafa,#dcdcdc);border-radius:0 0 14px 14px;margin:0 3px;font-size:19px;font-weight:700;color:#333;padding:13px 0 0 21px}
.card h2 span{color:var(--link-blue)}
.card p{font-size:13px;line-height:18px;color:#333}
.card-body{padding:16px 22px 0 22px;hyphens:auto}
.card-body p+p{margin-top:18px}
.help-icon{position:absolute;right:20px;top:66px}
.feature{position:relative;padding-left:56px;margin-bottom:14px}
.feature svg{position:absolute;left:0;top:0}
.feature strong{display:block;font-size:13px}
.feature i{font-size:13px;line-height:18px}

.clients{position:absolute;left:23px;top:780px;width:688px;height:180px;background:#fff;border:1px solid var(--card-border);border-radius:10px}
.clients h3{position:absolute;left:15px;top:26px;font-size:19px;font-weight:400;color:var(--link-blue)}
.quote-icon{position:absolute;left:612px;top:12px}
.client-name{position:absolute;top:78px;font-size:16px;font-weight:700;color:#888;white-space:nowrap;display:flex;align-items:center;gap:8px}
.client-name::before{content:"";width:14px;height:14px;background:#999}
.quotes{position:absolute;left:15px;top:115px;display:flex;gap:22px}
.quotes p{width:206px;font-size:12px;line-height:18px;color:#444}
.quotes .mark{color:var(--accent-orange)}

.side{position:absolute;left:734px;top:804px;width:212px}
.tabs{display:flex;align-items:flex-end;gap:12px;border-bottom:1px solid #ccc;height:38px}
.tab{width:60px;height:38px;border:1px solid #ccc;border-bottom:none;border-radius:6px 6px 0 0;background:#fff;font-size:17px;color:#444;text-align:center;padding-top:9px}
.social{width:26px;height:26px;border-radius:4px;margin-bottom:5px}
.social.a{background:#3b5a9a}.social.b{background:#4fb7e6}
.side h4{margin-top:12px;font-size:19px;font-weight:400;line-height:24px;color:var(--link-blue)}
.side p{margin-top:10px;font-size:12px;line-height:15px;color:#555}
</style>
</head>
<body>
<div class="page">
  <header class="header">
    <div class="logo">BRELLOWAY</div>
    <nav class="nav"><span>Services</span><span>SEO Case Studies</span><span>Contact Brelloway</span></nav>
    <div class="phone">Call 303-555-0142</div>
  </header>

  <section class="hero">
    <div class="hero-backdrop" role="img" aria-label="Faint blurred web address lettering in lavender tones"></div>
    <div class="hero-photo" role="img" aria-label="Photo of a businesswoman with a clipboard giving a thumbs up"></div>
    <div class="hero-arrow" style="top:44px" role="img" aria-label="Hand-drawn red arrow pointing to the search box"></div>
    <div class="hero-arrow" style="top:186px" role="img" aria-label="Hand-drawn red arrow pointing to the search box"></div>
    <div class="search"><span>eg. domain or keyword</span><div class="search-btn">Submit &amp;<br>Get Rankings</div></div>
    <h1 class="offer">Affordable as low<br>as <em>$99</em> per keyword</h1>
    <p class="offer-copy">Lorem ipsum dolor sit amet, consectetur adipiscing elit. Quisque pharetra, est a aliquam sollicitudin, dui ligula mollis diam, sit amet aliquam sapien nisl sit amet mauris.</p>
  </section>

  <section class="stats">
    <div class="stats-lead">In the Last 30 Days<br>We've Helped Generate</div>
    <svg class="stats-chevron" width="40" height="66" viewBox="0 0 40 66"><path d="M0 0h16l22 33-22 33H0l22-33z" fill="#fff" opacity=".9"/></svg>
    <div class="stat" style="left:348px"><b>2,306,923</b>Leads</div>
    <div class="stat-divider" style="left:508px"></div>
    <div class="stat" style="left:550px"><b>$49,338,574</b>in E-Commerce Sales</div>
    <div class="stat-divider" style="left:745px"></div>
    <div class="stat" style="left:787px"><b>46,376,640</b>Search Visits</div>
  </section>

  <article class="card" style="left:23px">
    <h2>Who needs <span>Brelloway?</span></h2>
    <div class="card-body">
      <p>Lorem ipsum dolor sit amet, consectetur adipiscing elit. Quisque pharetra, est a aliquam sollicitudin, dui ligula mollis diam, sit amet aliquam sapien nisl sit amet mauris. Nulla purus dui, varius ac ultrices et, ullamcor&shy;per ut mauris.</p>
      <p>Nullam felis velit, hendrerit a aliquet at, interdum sit amet ligula. Phasellus sceleris&shy;que tristique lectus, sit amet gravida enim suscipit nec. Integer vehicula imperdiet nunc sodales volutpat.</p>
    </div>
  </article>

  <article class="card" style="left:341px">
    <h2>How does <span>Brelloway</span> work?</h2>
    <svg class="help-icon" width="82" height="82" viewBox="0 0 82 82">
      <circle cx="41" cy="41" r="39" fill="#eee" stroke="#ccc"/>
      <circle cx="41" cy="41" r="31" fill="#1a7bd6"/>
      <text x="41" y="55" text-anchor="middle" font-family="Arimo,sans-serif" font-weight="700" font-size="40" fill="#fff">?</text>
    </svg>
    <div class="card-body" style="padding-right:112px">
      <p>Ut commodo, mi in ultricies bibendum, enim diam congue felis, a auctor ipsum est a urna. Etiam purus felis, vestibulum a ornare ac, posuere id nisl.</p>
    </div>
    <div class="card-body" style="padding-top:16px">
      <p>Ut rutrum urna at felis bibendum vitae congue lectus porttitor. Nulla tincidunt erat sit amet diam pellentesque ac aliquet sem placerat. Quisque non condimentum nisl. Integer fringilla volutpat velit.</p>
    </div>
  </article>

  <article class="card" style="left:659px">
    <h2><span>Easy</span> and <span>Affordable</span></h2>
    <div class="card-body" style="padding-left:18px">
      <div class="feature"><svg width="44" height="40" viewBox="0 0 44 40"><rect x="2" y="2" width="40" height="28" rx="2" fill="#ddd" stroke="#999"/><rect x="6" y="6" width="32" height="20" fill="#333"/><rect x="16" y="31" width="12" height="6" fill="#bbb"/></svg><strong>Easy to Install</strong><i>Lorem ipsum dolor sit amet, con&shy;sectetur adipiscing elit.</i></div>
      <div class="feature"><svg width="40" height="40" viewBox="0 0 40 40"><rect x="4" y="4" width="32" height="32" fill="#fff" stroke="#bbb"/><path d="M8 30l8-10 7 5 9-14" stroke="#e04b2b" stroke-width="2" fill="none"/><path d="M8 24l8 2 7-8 9 4" stroke="#3a8be0" stroke-width="2" fill="none"/></svg><strong>Easy on your wallet</strong><i>Duis aliquam porttitor augue at porttitor. Morbi cursus mollis enim eget laoreet.</i></div>
      <div class="feature"><svg width="40" height="40" viewBox="0 0 40 40"><circle cx="20" cy="20" r="18" fill="#f0a21a"/><text x="20" y="28" text-anchor="middle" font-family="Arimo,sans-serif" font-weight="700" font-size="22" fill="#fff">i</text></svg><strong>Easy to delight</strong><i>Sed suscipit libero at tortor porta imperdiet vitae luctus est.</i></div>
    </div>
  </article>

  <section class="clients">
    <h3>Innovative Companies Choose Brelloway for their SEO</h3>
    <svg class="quote-icon" width="60" height="46" viewBox="0 0 60 46"><rect x="0" y="0" width="36" height="26" rx="4" fill="#2f6fc4"/><path d="M8 26v8l8-8z" fill="#2f6fc4"/><rect x="18" y="12" width="40" height="26" rx="4" fill="#4d8ddc"/><path d="M48 38v8l-8-8z" fill="#4d8ddc"/></svg>
    <div class="client-name" style="left:21px">Norvane</div>
    <div class="client-name" style="left:161px">The Halden Group</div>
    <div class="client-name" style="left:339px">Solvexa</div>
    <div class="client-name" style="left:488px">Pinecrest Links</div>
    <div class="quotes">
      <p><span class="mark">"</span>With Brelloway's help and expertise, we are generating more revenue than at any other time in our corporate history and our results keep growing.</p>
      <p><span class="mark">"</span>Without a doubt my marketing investment with Brelloway is the best money I've ever spent. I have enjoyed steady leads every month since.</p>
      <p><span class="mark">"</span>When we needed a comprehensive social marketing campaign we turned to our current SEO provider Brelloway, and they delivered fast.</p>
    </div>
  </section>

  <aside class="side">
    <div class="tabs"><div class="tab">Blog</div><div class="social a"></div><div class="social b"></div></div>
    <h4>SEO Services /<br>Webdesign Services</h4>
    <p>What are the latest trends in Internet Marketing, what's better microblogs, social pages, deal sites, search offers</p>
  </aside>
</div>
</body>
</html>
```